New Business Card for General Contractor Marketing

Need a business card the is more like a marketing promotion of our services
Must be horizontal orientation, One Sided Only, Max font size, Organize the Services
#1 General Contractor for Realtors
Remodels – Renovations – Repairs
Water & Mold Damage Experts
Painting: Interior/ Exterior
Flooring: Wood / LVT / Carpet
Plumbing: Repairs & Upgrades
Electric: Lights & Energy Efficient Upgrades
Kitchen & Bath Remodels
Fast Inspections Repair Billed Thru Escrow
BrightHarborBuilds.com
555-418-2796

Industry/Entity Type

General Contractor

Contact Information for Business Card

One Sided Only: #1 General Contractor for Realtors Remodels – Renovations – Repairs Water & Mold Damage Experts Painting: Interior/ Exterior Flooring: Wood / LVT / Carpet Plumbing: Repairs & Upgrades Electric: Lights & Energy Efficient Upgrades Kitchen & Bath Remodels Fast Inspections Repair Billed Thru Escrow BrightHarborBuilds.com 555-418-2796

Colors
0054AA
0677BA
7BADD7
CADEEF
E8F1F8

Requirements
Must have
• One Sided Only: #1 General Contractor for Realtors Remodels – Renovations – Repairs Water & Mold Damage Experts Painting: Interior/ Exterior Flooring: Wood / LVT / Carpet Plumbing: Repairs & Upgrades Electric: Lights & Energy Efficient Upgrades Kitchen & Bath Remodels Fast Inspections Repair Billed Thru Escrow BrightHarborBuilds.com 555-418-2796

```html
<!DOCTYPE html>
<html lang="en">
<head>
<meta charset="utf-8">
<title>General Contractor for Realtors – Business Card</title>
<link rel="stylesheet" href="https://fonts.googleapis.com/css2?family=Roboto+Condensed:wght@700;800&family=Orbitron:wght@700&family=Arimo:wght@400&display=swap">
<style>
  :root {
    --backdrop: #ebebeb;
    --card-white: #ffffff;
    --brand-navy: #1b2a52;
    --brand-orange: #f58220;
    --ink: #111111;
    --light: #ffffff;
  }
  * { box-sizing: border-box; margin: 0; padding: 0; }
  html, body { width: 1200px; height: 1200px; overflow: hidden; }
  body {
    background: var(--backdrop);
    position: relative;
    font-family: "Roboto Condensed", "Arial Narrow", sans-serif;
  }
  .card {
    position: absolute;
    left: 235px;
    width: 731px;
    border-radius: 30px;
    overflow: hidden;
  }
  .card--front { top: 157px; height: 413px; background: var(--card-white); }
  .card--back  { top: 650px; height: 417px; background: var(--brand-navy); }

  .brand-name {
    position: absolute;
    left: 0; right: 0;
    text-align: center;
    font-weight: 800;
    font-size: 34px;
    letter-spacing: 0.5px;
    line-height: 1;
  }
  .card--front .brand-name { top: 50px; color: var(--brand-navy); }
  .card--back  .brand-name { top: 150px; color: var(--light); }

  .headline {
    position: absolute;
    left: 0; right: 0;
    text-align: center;
    font-weight: 800;
    font-size: 39px;
    line-height: 1;
    transform: scaleX(0.92);
  }
  .tagline {
    position: absolute;
    left: 0; right: 0;
    text-align: center;
    font-weight: 800;
    font-size: 24px;
    line-height: 1;
  }
  .card--front .headline { top: 124px; color: var(--ink); }
  .card--front .tagline  { top: 169px; color: var(--ink); }
  .card--back .headline  { top: 220px; color: var(--light); }
  .card--back .tagline   { top: 265px; color: var(--light); }

  .services {
    position: absolute;
    top: 198px; left: 0; right: 0;
    height: 102px;
    background: var(--brand-orange);
    padding-top: 13px;
    list-style: none;
    text-align: center;
  }
  .services li {
    color: var(--brand-navy);
    font-weight: 700;
    font-size: 19px;
    line-height: 25.5px;
  }
  .escrow-band {
    position: absolute;
    top: 300px; left: 0; right: 0;
    height: 35px;
    background: var(--brand-navy);
    color: var(--light);
    font-weight: 700;
    font-size: 18px;
    line-height: 35px;
    text-align: center;
  }
  .phone {
    position: absolute;
    top: 348px; left: 0; right: 0;
    text-align: center;
    font-family: "Orbitron", sans-serif;
    font-weight: 700;
    font-size: 31px;
    letter-spacing: 1.5px;
    color: var(--brand-orange);
    line-height: 1;
  }
  .website {
    position: absolute;
    top: 383px; left: 0; right: 0;
    text-align: center;
    font-family: "Arimo", Arial, sans-serif;
    font-size: 15px;
    color: var(--ink);
    line-height: 1;
  }
</style>
</head>
<body>
  <section class="card card--front">
    <div class="brand-name">Bright Harbor Builds</div>
    <h1 class="headline">General Contractor for Realtors</h1>
    <p class="tagline">Remodels – Renovations – Repairs</p>
    <ul class="services">
      <li>•&nbsp; Water &amp; Mold Damage Experts • Painting: Interior/ Exterior</li>
      <li>• Flooring: Wood / LVT / Carpet • Plumbing: Repairs &amp; Upgrades</li>
      <li>• Electric: Lights &amp; Energy Efficient Upgrades • Kitchen &amp; Bath Remodels</li>
    </ul>
    <div class="escrow-band">Fast Inspections Repair Billed Thru Escrow</div>
    <div class="phone">CALL&nbsp; 555-418-2796</div>
    <div class="website">BrightHarborBuilds.com</div>
  </section>

  <section class="card card--back">
    <div class="brand-name">Bright Harbor Builds</div>
    <h2 class="headline">General Contractor for Realtors</h2>
    <p class="tagline">Remodels – Renovations – Repairs</p>
  </section>
</body>
</html>
```